R Bawden Consulting Design

Our company is a multi-faceted consulting service in specialized areas such as project management and event management.
I would like the design to utilise the colour green, but be simple and unique in concept.
The design should communicate collaboration, openness, trust, efficiency and professionalism.
We like the idea of cogs in a wheel or other geometric designs.

Target Market(s)

Target market is large corporate manufacturers.

Industry/Entity Type

Wheel

Contact Information for Business Card

R Bawden Consulting
Marlene Bawden
Ph. 0492 654 071
Email. marlyfoster@velmarnet.example.net
Address. 7 Tarrow Ct, Brenfield Vic 3987 Australia

```html
<!DOCTYPE html>
<html lang="en">
<head>
<meta charset="utf-8">
<title>R Bawden Consulting – Business Card</title>
<link rel="stylesheet" href="https://fonts.googleapis.com/css2?family=Exo+2:wght@600&family=Open+Sans:wght@400;600&display=swap">
<style>
  :root {
    --navy: #2b2d7c;
    --green: #8cc63f;
    --white: #ffffff;
    --black: #050505;
    --backdrop: #e6e4e0;
    --card-w: 880px;
    --card-h: 538px;
  }
  * { box-sizing: border-box; margin: 0; padding: 0; }
  html, body { width: 1200px; height: 1200px; overflow: hidden; }
  body {
    background: var(--backdrop);
    display: flex;
    flex-direction: column;
    align-items: center;
    justify-content: center;
    gap: 40px;
  }
  .card {
    position: relative;
    width: var(--card-w);
    height: var(--card-h);
    overflow: hidden;
    box-shadow: 0 6px 18px rgba(0,0,0,.18);
    background: var(--navy);
  }
  .card-art { position: absolute; inset: 0; width: 100%; height: 100%; }

  .illustration {
    position: absolute;
    border-radius: 50%;
  }
  .illustration-white { background: var(--white); }
  .illustration-green { background: var(--green); }
  .card-front .illustration-white { left: -152px; top: -182px; width: 444px; height: 444px; }
  .card-front .illustration-green { left: 190px; top: 230px; width: 200px; height: 200px; }
  .card-back .illustration-white { left: 700px; top: 200px; width: 400px; height: 400px; }
  .card-back .illustration-green { left: 530px; top: 40px; width: 160px; height: 160px; }

  .brand {
    position: absolute;
    display: flex;
    align-items: center;
    gap: 18px;
    font-family: "Exo 2", sans-serif;
    font-weight: 600;
    color: var(--white);
    text-transform: uppercase;
    line-height: 1.02;
    letter-spacing: 1px;
  }
  .brand-mark { width: 70px; height: 70px; background: var(--green); flex: none; }
  .brand-name { font-size: 44px; }
  .card-front .brand { left: 420px; top: 180px; }
  .card-back .brand { left: 60px; top: 55px; }

  .contact {
    position: absolute;
    left: 70px;
    top: 340px;
    font-family: "Open Sans", sans-serif;
    color: var(--white);
  }
  .contact-name {
    font-weight: 600;
    font-size: 29px;
    color: var(--green);
    text-transform: uppercase;
    margin: 0 0 10px 22px;
  }
  .contact-list { list-style: none; }
  .contact-line {
    display: flex;
    align-items: center;
    gap: 12px;
    font-size: 21px;
    height: 40px;
    white-space: nowrap;
  }
  .contact-line svg { width: 22px; height: 22px; fill: var(--white); flex: none; }
</style>
</head>
<body>

<section class="card card-front" aria-label="Business card front">
  <div class="illustration illustration-white" role="img" aria-label="Large white gear illustration"></div>
  <div class="illustration illustration-green" role="img" aria-label="Small green gear illustration"></div>
  <div class="brand">
    <span class="brand-mark"></span>
    <span class="brand-name">R Bawden<br>Consulting</span>
  </div>
</section>

<section class="card card-back" aria-label="Business card back">
  <svg class="card-art" viewBox="0 0 880 538" aria-hidden="true">
    <rect class="contact-band" x="0" y="290" width="880" height="248" fill="var(--black)"/>
    <circle class="illustration-surround" cx="900" cy="400" r="250" fill="var(--navy)"/>
  </svg>
  <div class="illustration illustration-white" role="img" aria-label="Large white gear illustration"></div>
  <div class="illustration illustration-green" role="img" aria-label="Small green gear illustration"></div>
  <div class="brand">
    <span class="brand-mark"></span>
    <span class="brand-name">R Bawden<br>Consulting</span>
  </div>
  <div class="contact">
    <p class="contact-name">Marlene Bawden</p>
    <ul class="contact-list">
      <li class="contact-line">
        <svg viewBox="0 0 24 24" aria-label="Phone"><path d="M3 9c0-3 4-5 9-5s9 2 9 5l-1 2-4-1v-2c-2-.6-6-.6-8 0v2l-4 1zM7 12h10l2 8H5zm5 2.5a2.5 2.5 0 100 5 2.5 2.5 0 000-5z"/></svg>
        <span>0492 654 071</span>
      </li>
      <li class="contact-line">
        <svg viewBox="0 0 24 24" aria-label="Email"><path d="M2 5h20v14H2zm2 2v.5l8 6 8-6V7zm0 3v7h16v-7l-8 6z"/></svg>
        <span>marlyfoster@velmarnet.example.net</span>
      </li>
      <li class="contact-line">
        <svg viewBox="0 0 24 24" aria-label="Address"><path d="M12 3l10 9h-3v9h-5v-6h-4v6H5v-9H2z"/></svg>
        <span>7 Tarrow Ct, Brenfield Vic 3987 Australia</span>
      </li>
    </ul>
  </div>
</section>

</body>
</html>
```